Cravo Azul - Apresentação de nova plataforma de bilhética

Precisamos de uma apresentação do novo negócio para diferentes targets. Anexo briefing, logo e imagens tipo a usar.

```html
<!DOCTYPE html>
<html lang="pt">
<head>
<meta charset="utf-8">
<title>Cravo Azul — Apresentação</title>
<link href="https://fonts.googleapis.com/css2?family=Outfit:wght@400;500;600;700&display=swap" rel="stylesheet">
<style>
  :root{
    --red:#e31e24;
    --ink:#111111;
    --line:#1a1a1a;
    --soft-line:#c8c8c8;
    --crowd:#e2e2e2;
    --paper:#ffffff;
  }
  *{margin:0;padding:0;box-sizing:border-box}
  html,body{width:1200px;height:860px;overflow:hidden;background:var(--paper)}
  body{font-family:"Outfit",sans-serif;color:var(--ink);position:relative}
  .board{position:absolute;left:54px;top:67px;width:1092px;height:727px;border:2px solid var(--line)}
  .abs{position:absolute;line-height:1;white-space:nowrap}
  .red{color:var(--red)}
  .rule{position:absolute;background:var(--line)}
  .rule-soft{position:absolute;background:var(--soft-line)}

  /* brand block */
  .brand-mark{position:absolute;left:151px;top:136px;width:34px;height:34px;background:var(--red)}
  .brand-name{left:140px;top:182px;font-size:25px;font-weight:700;color:var(--ink)}
  .hero-title{left:136px;top:236px;font-size:24px;font-weight:500;line-height:1.1}
  .hero-title span{display:block}
  .hero-title span+span{padding-left:5px}
  .hero-free{left:142px;top:301px;font-size:28px;font-weight:700;color:var(--red)}
  .hero-sub{left:140px;top:337px;font-size:12px;font-weight:500}
  .hero-note{left:140px;top:356px;font-size:8.6px;font-weight:500;line-height:1.7}

  .collage{position:absolute;left:307px;top:99px}

  /* event types */
  .types-title{left:790px;top:135px;font-size:17.5px;font-weight:500}
  .type{position:absolute;width:80px;text-align:center}
  .type svg{display:block;margin:0 auto;width:36px;height:36px}
  .type-label{display:block;margin-top:14px;font-size:8.5px;font-weight:500}

  /* target & positioning */
  .section-head{font-size:14px;font-weight:600;color:var(--red)}
  .check-list{position:absolute;list-style:none}
  .check-list li{display:flex;align-items:center;font-weight:500;white-space:nowrap}
  .check-list svg{flex:none;margin-right:7px}
  .target-list{left:145px;top:446px}
  .target-list li{height:17.5px;font-size:10.5px}
  .target-list svg{width:11px;height:11px}
  .position-text{left:452px;top:449px;font-size:15.5px;font-weight:500;line-height:27.4px}
  .position-text span{display:block}

  .crowd{position:absolute;left:645px;top:444px}
  .deco-name{left:770px;top:454px;font-size:34px;font-weight:700;color:var(--red)}
  .deco-dot{position:absolute;left:770px;top:428px;width:18px;height:18px;border-radius:50%;background:var(--red)}

  /* baselines */
  .bl-head{font-size:14px;font-weight:500}
  .promo-list li{height:20.3px;font-size:9px}
  .promo-list svg{width:11px;height:11px;margin-right:8px}
  .promo-a{left:145px;top:623px}
  .promo-b{left:400px;top:626px}
  .promo-b li{height:23.5px}
  .client-text{left:648px;top:648px;font-size:9px;font-weight:500;line-height:16.5px}
  .client-text span{display:block}
  .client-calls{position:absolute;left:862px;top:615px;list-style:none}
  .client-calls li{display:flex;align-items:center;height:28px;font-size:15.5px;font-weight:500;color:var(--red);white-space:nowrap}
  .client-calls svg{width:18px;height:18px;margin-right:16px;flex:none}
  .client-calls .sq{width:14px;height:14px;border:1.3px solid var(--red);margin:0 18px 0 2px;flex:none}
</style>
</head>
<body>
  <div class="board"></div>

  <!-- brand / hero -->
  <div class="brand-mark"></div>
  <div class="abs brand-name">Cravo Azul</div>
  <div class="abs hero-title"><span>Venda os seus</span><span>ingressos online</span></div>
  <div class="abs hero-free">GRÁTIS</div>
  <div class="abs hero-sub">Simples e rápido</div>
  <div class="abs hero-note">Desenhado para pequenos e médios<br>eventos em Portugal.</div>

  <svg class="collage" width="426" height="303" viewBox="0 0 426 303">
    <defs>
      <linearGradient id="g-fest" x1="0" y1="0" x2="0" y2="1"><stop offset="0" stop-color="#6b4a2a"/><stop offset=".5" stop-color="#3b2a1e"/><stop offset="1" stop-color="#1c1512"/></linearGradient>
      <linearGradient id="g-screen" x1="0" y1="0" x2="0" y2="1"><stop offset="0" stop-color="#3a6bd8"/><stop offset=".6" stop-color="#1a2f8a"/><stop offset="1" stop-color="#0e1a55"/></linearGradient>
      <linearGradient id="g-stage" x1="0" y1="0" x2="0" y2="1"><stop offset="0" stop-color="#1a1410"/><stop offset=".6" stop-color="#5a3f22"/><stop offset="1" stop-color="#2a1d12"/></linearGradient>
      <linearGradient id="g-solo" x1="0" y1="0" x2="0" y2="1"><stop offset="0" stop-color="#3b1d4d"/><stop offset=".5" stop-color="#b0285e"/><stop offset="1" stop-color="#4b1638"/></linearGradient>
      <linearGradient id="g-street" x1="0" y1="0" x2="0" y2="1"><stop offset="0" stop-color="#cfd6d8"/><stop offset=".45" stop-color="#6f8460"/><stop offset="1" stop-color="#5b5a58"/></linearGradient>
    </defs>
    <g role="img" aria-label="Fotografia de festa popular ao ar livre com bandeirinhas coloridas e multidão"><polygon points="67,0 265,0 230,155 33,155" fill="url(#g-fest)"/></g>
    <g role="img" aria-label="Fotografia de sala de conferências com público diante de um ecrã"><polygon points="269,0 426,0 426,154 233,154" fill="url(#g-screen)"/></g>
    <g role="img" aria-label="Fotografia de elenco de teatro em palco"><polygon points="32,159 190,159 161,303 0,303" fill="url(#g-stage)"/></g>
    <g role="img" aria-label="Fotografia de artista em palco com luzes vermelhas e roxas"><polygon points="194,159 313,159 290,303 164,303" fill="url(#g-solo)"/></g>
    <g role="img" aria-label="Fotografia de feira de rua com tendas e visitantes"><polygon points="316,159 426,159 426,303 292,303" fill="url(#g-street)"/></g>
  </svg>

  <!-- event types -->
  <div class="abs types-title">Para <span class="red">todos</span> os tipos de <span class="red">eventos</span></div>

  <div class="rule-soft" style="left:828px;top:190px;width:1px;height:68px"></div>
  <div class="rule-soft" style="left:921px;top:190px;width:1px;height:68px"></div>
  <div class="rule-soft" style="left:1005px;top:190px;width:1px;height:68px"></div>
  <div class="rule-soft" style="left:766px;top:275px;width:300px;height:1px"></div>
  <div class="rule-soft" style="left:828px;top:296px;width:1px;height:68px"></div>
  <div class="rule-soft" style="left:921px;top:296px;width:1px;height:68px"></div>
  <div class="rule-soft" style="left:1005px;top:296px;width:1px;height:68px"></div>

  <div class="type" style="left:741px;top:192px">
    <svg viewBox="0 0 36 36" fill="none" stroke="var(--red)" stroke-width="1.6"><circle cx="8" cy="29" r="4"/><circle cx="28" cy="25" r="4"/><path d="M12 29V9l20-5v21M12 14l20-5"/></svg>
    <span class="type-label">Música</span>
  </div>
  <div class="type" style="left:830px;top:192px">
    <svg viewBox="0 0 36 36" fill="none" stroke="var(--red)" stroke-width="1.6"><path d="M3 4h30M5 4v26c5 0 9-6 9-14V4M31 4v26c-5 0-9-6-9-14V4M3 32h30"/></svg>
    <span class="type-label">Teatro</span>
  </div>
  <div class="type" style="left:919px;top:192px">
    <svg viewBox="0 0 36 36" fill="none" stroke="var(--red)" stroke-width="1.6"><rect x="4" y="13" width="28" height="20"/><path d="M4 13l-1-6 27-5 1 6z"/><path d="M15 18v10l8-5z"/></svg>
    <span class="type-label">Cinema</span>
  </div>
  <div class="type" style="left:1006px;top:192px">
    <svg viewBox="0 0 36 36" fill="none" stroke="var(--red)" stroke-width="1.6"><circle cx="23" cy="13" r="6"/><path d="M19 17L8 32l3 2 13-13M24 24l6 6"/></svg>
    <span class="type-label">Comédia</span>
  </div>

  <div class="type" style="left:743px;top:296px">
    <svg viewBox="0 0 36 36" fill="none" stroke="var(--red)" stroke-width="1.6"><path d="M3 33l9-20 11 11z"/><path d="M18 12l4-8M23 16l8-4M26 22h8M14 6l1-4M30 5l2-2"/></svg>
    <span class="type-label">Festas</span>
  </div>
  <div class="type" style="left:830px;top:296px">
    <svg viewBox="0 0 36 36" fill="none" stroke="var(--red)" stroke-width="1.6"><rect x="10" y="2" width="24" height="14"/><circle cx="6" cy="9" r="2.5"/><circle cx="8" cy="24" r="2.5"/><circle cx="18" cy="24" r="2.5"/><circle cx="28" cy="24" r="2.5"/><path d="M3 34c0-4 2-6 5-6s5 2 5 6M13 34c0-4 2-6 5-6s5 2 5 6M23 34c0-4 2-6 5-6s5 2 5 6"/></svg>
    <span class="type-label">Workshops</span>
  </div>
  <div class="type" style="left:917px;top:296px">
    <svg viewBox="0 0 36 36" fill="none" stroke="var(--red)" stroke-width="1.6"><path d="M8 14h20v4H8zM11 18h14v12H11zM7 30h22v4H7zM18 14V6"/><circle cx="18" cy="4" r="2"/></svg>
    <span class="type-label">Conferências</span>
  </div>
  <div class="type" style="left:1006px;top:296px">
    <svg viewBox="0 0 36 36" fill="none" stroke="var(--red)" stroke-width="1.6"><path d="M2 13L18 3l16 10M4 13h28v4H4zM5 17v17h26V17M2 34h32"/><circle cx="12" cy="23" r="2"/><circle cx="24" cy="23" r="2"/><path d="M9 34c0-4 1-6 3-6s3 2 3 6M21 34c0-4 1-6 3-6s3 2 3 6"/></svg>
    <span class="type-label">Feiras</span>
  </div>

  <div class="rule" style="left:103px;top:402px;width:994px;height:1px"></div>

  <!-- target -->
  <div class="abs section-head" style="left:145px;top:424px">Target</div>
  <ul class="check-list target-list">
    <li><svg viewBox="0 0 12 12" fill="none" stroke="var(--red)" stroke-width="1.1"><circle cx="6" cy="6" r="5.3"/><path d="M3.5 6.2l1.7 1.6 3.4-3.5"/></svg>Pequenas autarquias</li>
    <li><svg viewBox="0 0 12 12" fill="none" stroke="var(--red)" stroke-width="1.1"><circle cx="6" cy="6" r="5.3"/><path d="M3.5 6.2l1.7 1.6 3.4-3.5"/></svg>Coletividades</li>
    <li><svg viewBox="0 0 12 12" fill="none" stroke="var(--red)" stroke-width="1.1"><circle cx="6" cy="6" r="5.3"/><path d="M3.5 6.2l1.7 1.6 3.4-3.5"/></svg>Associações</li>
    <li><svg viewBox="0 0 12 12" fill="none" stroke="var(--red)" stroke-width="1.1"><circle cx="6" cy="6" r="5.3"/><path d="M3.5 6.2l1.7 1.6 3.4-3.5"/></svg>Teatros e cinemas locais</li>
    <li><svg viewBox="0 0 12 12" fill="none" stroke="var(--red)" stroke-width="1.1"><circle cx="6" cy="6" r="5.3"/><path d="M3.5 6.2l1.7 1.6 3.4-3.5"/></svg>Promotores culturais</li>
    <li><svg viewBox="0 0 12 12" fill="none" stroke="var(--red)" stroke-width="1.1"><circle cx="6" cy="6" r="5.3"/><path d="M3.5 6.2l1.7 1.6 3.4-3.5"/></svg>Eventos universitários</li>
  </ul>
  <div class="rule" style="left:397px;top:426px;width:1px;height:126px"></div>

  <!-- positioning -->
  <div class="abs section-head" style="left:452px;top:424px">Posicionamento</div>
  <div class="abs position-text">
    <span>A plataforma portuguesa</span>
    <span>de bilhética <span class="red" style="display:inline">simples, rápida</span></span>
    <span class="red">e sem complicações <span style="display:inline;color:var(--ink)">para</span></span>
    <span>pequenos e médios eventos.</span>
  </div>

  <svg class="crowd" width="452" height="131" viewBox="0 0 452 131" role="img" aria-label="Silhueta clara de multidão com braços no ar">
    <defs><linearGradient id="g-crowd" x1="0" y1="0" x2="1" y2="0"><stop offset="0" stop-color="var(--crowd)" stop-opacity=".2"/><stop offset=".4" stop-color="var(--crowd)"/><stop offset="1" stop-color="var(--crowd)"/></linearGradient></defs>
    <rect x="0" y="0" width="452" height="131" fill="url(#g-crowd)" opacity=".55"/>
  </svg>
  <div class="deco-dot"></div>
  <div class="abs deco-name">Cravo Azul</div>

  <div class="rule" style="left:103px;top:575px;width:994px;height:1px"></div>
  <div class="rule" style="left:599px;top:575px;width:1px;height:187px"></div>

  <!-- baselines promotores -->
  <div class="abs bl-head" style="left:146px;top:593px">Baselines - <span class="red">Promotores</span></div>
  <ul class="check-list promo-list promo-a">
    <li><svg viewBox="0 0 12 12" fill="none" stroke="var(--red)" stroke-width="1.1"><circle cx="6" cy="6" r="5.3"/><path d="M3.5 6.2l1.7 1.6 3.4-3.5"/></svg>Comece a vender bilhetes grátis</li>
    <li><svg viewBox="0 0 12 12" fill="none" stroke="var(--red)" stroke-width="1.1"><circle cx="6" cy="6" r="5.3"/><path d="M3.5 6.2l1.7 1.6 3.4-3.5"/></svg>Venda bilhetes online sem complicações</li>
    <li><svg viewBox="0 0 12 12" fill="none" stroke="var(--red)" stroke-width="1.1"><circle cx="6" cy="6" r="5.3"/><path d="M3.5 6.2l1.7 1.6 3.4-3.5"/></svg>Crie o evento e comece logo a vender.</li>
    <li><svg viewBox="0 0 12 12" fill="none" stroke="var(--red)" stroke-width="1.1"><circle cx="6" cy="6" r="5.3"/><path d="M3.5 6.2l1.7 1.6 3.4-3.5"/></svg>Crie o seu evento em minutos.</li>
    <li><svg viewBox="0 0 12 12" fill="none" stroke="var(--red)" stroke-width="1.1"><circle cx="6" cy="6" r="5.3"/><path d="M3.5 6.2l1.7 1.6 3.4-3.5"/></svg>Receba pagamentos de forma simples e segura.</li>
  </ul>
  <div class="rule" style="left:381px;top:612px;width:1px;height:93px"></div>
  <ul class="check-list promo-list promo-b">
    <li><svg viewBox="0 0 12 12" fill="none" stroke="var(--red)" stroke-width="1.1"><circle cx="6" cy="6" r="5.3"/><path d="M3.5 6.2l1.7 1.6 3.4-3.5"/></svg>O palco é teu. A bilheteira é nossa.</li>
    <li><svg viewBox="0 0 12 12" fill="none" stroke="var(--red)" stroke-width="1.1"><circle cx="6" cy="6" r="5.3"/><path d="M3.5 6.2l1.7 1.6 3.4-3.5"/></svg>Criar eventos nunca foi tão simples.</li>
    <li><svg viewBox="0 0 12 12" fill="none" stroke="var(--red)" stroke-width="1.1"><circle cx="6" cy="6" r="5.3"/><path d="M3.5 6.2l1.7 1.6 3.4-3.5"/></svg>Receba pagamentos rapidamente.</li>
  </ul>

  <!-- baselines clientes -->
  <div class="abs bl-head" style="left:651px;top:593px">Baselines – <span class="red">Clientes</span></div>
  <div class="abs client-text"><span>O teu bilhete para todos os momentos.</span><span>Hoje sais de casa.</span></div>
  <div class="rule" style="left:828px;top:619px;width:1px;height:107px"></div>
  <ul class="client-calls">
    <li><span class="sq"></span>“Reserva já.”</li>
    <li><svg viewBox="0 0 20 20" fill="none" stroke="var(--red)" stroke-width="1.2"><path d="M10 17S2 12 2 7a4 4 0 0 1 8-1 4 4 0 0 1 8 1c0 5-8 10-8 10z"/></svg>“Vive já.”</li>
    <li><svg viewBox="0 0 20 20" fill="none" stroke="var(--red)" stroke-width="1.2"><circle cx="8" cy="8" r="6"/><path d="M12.5 12.5L19 19"/></svg>“Descobre já.”</li>
    <li><svg viewBox="0 0 20 20" fill="none" stroke="var(--red)" stroke-width="1.2"><path d="M10 1.5l2.6 5.4 5.9.8-4.3 4.1 1 5.8L10 14.8l-5.2 2.8 1-5.8L1.5 7.7l5.9-.8z"/></svg>“Acontece já.”</li>
  </ul>

  <div class="rule" style="left:103px;top:762px;width:994px;height:1px"></div>
</body>
</html>
```